Party invitation with a difference

I have recently turned 65, and I am holding a party for a number of my friends

I am looking for a stylish party invitation possibly in the guise of a rock concert admission ticket./ poster

promoting my band Blue Kettle who will be playing.at the party. We are a middle of the road covers band

I am turning 65 years so something like 65 and still Rocking ...

The party will run from 7.00pm until 11.00pm

Food platter and drink supplied.

No presents please

Date Saturday 30 June 2018
At Marlow & Fenn Restaurant, 718, Pebble Lane. Clevedon, Auckland 2617

RSVP to dennis.halloway@wirefold.co.nz

Target Market(s)

I have a guest list

Font styles to use

Colors

Designer to choose colors to be used in the design.

Requirements
Must have
• I will want to email the invitation to my guests as well as be able to print some off .
Nice to have
• The invitation is from Dennis and Marjorie Halloway
Should not have
• Not be flowery

```html
<!DOCTYPE html>
<html lang="en">
<head>
<meta charset="utf-8">
<title>65 Years and Still Rocking – Dennis's Birthday Party</title>
<link rel="stylesheet" href="https://fonts.googleapis.com/css2?family=Anton&family=Michroma&family=Orbitron:wght@700;800&display=swap">
<style>
  :root {
    --page-bg: #d4d5d6;
    --ticket-dark: #0e0e0f;
    --ticket-mid: #222325;
    --rock-red: #ff1010;
    --bar-red: #5e0a0a;
    --white: #f4f4f4;
    --silver-light: #f2f2f2;
    --silver-dark: #8c8c8c;
    --guest-grey: #9d9d9d;
  }
  * { margin: 0; padding: 0; box-sizing: border-box; }
  html, body { width: 1200px; height: 848px; overflow: hidden; }
  body { background: var(--page-bg); position: relative; }

  .ticket {
    position: absolute;
    left: 50px; top: 195px;
    width: 1100px; height: 458px;
    color: var(--white);
  }
  .ticket-shape { position: absolute; inset: 0; width: 100%; height: 100%; }

  .age {
    position: absolute; left: 24px; top: 22px;
    font-family: "Anton", sans-serif; font-size: 128px; line-height: 1;
    background: linear-gradient(180deg, var(--silver-light) 0%, var(--silver-dark) 55%, var(--silver-light) 100%);
    -webkit-background-clip: text; background-clip: text; color: transparent;
  }
  .headline {
    position: absolute; left: 152px; top: 36px;
    font-family: "Anton", sans-serif; font-size: 58px; line-height: 1;
    text-transform: uppercase; letter-spacing: 0.5px;
    background: linear-gradient(180deg, var(--silver-light) 0%, #bdbdbd 60%, var(--silver-light) 100%);
    -webkit-background-clip: text; background-clip: text; color: transparent;
  }
  .party-title {
    position: absolute; left: 156px; top: 104px;
    font-family: "Orbitron", sans-serif; font-weight: 800; font-size: 34px; line-height: 1;
    font-variant: small-caps; color: var(--rock-red);
  }
  .rule { position: absolute; left: 30px; top: 166px; width: 752px; height: 3px; background: var(--white); }

  .guitar {
    position: absolute; left: 32px; top: 190px; width: 68px; height: 214px;
    background: var(--rock-red); border-radius: 10px 10px 30px 30px;
  }

  .details { position: absolute; left: 122px; top: 204px; width: 662px; }
  .detail-label {
    font-family: "Michroma", sans-serif; font-size: 13px; line-height: 1;
    text-transform: uppercase; color: var(--rock-red); padding-left: 12px; margin-bottom: 5px;
  }
  .detail-bar {
    background: var(--bar-red);
    font-family: "Michroma", sans-serif; font-size: 15px; line-height: 25px;
    font-variant: small-caps; padding: 0 12px; margin-bottom: 8px;
  }
  .detail-note {
    font-family: "Michroma", sans-serif; font-size: 15px; line-height: 1;
    font-variant: small-caps; padding-left: 12px; margin-top: 10px;
  }

  .vertical { position: absolute; writing-mode: vertical-rl; transform: rotate(180deg); line-height: 1; white-space: nowrap; }
  .guest-special { left: 872px; bottom: 50px; font-family: "Anton", sans-serif; font-size: 42px; color: var(--guest-grey); text-transform: uppercase; }
  .guest-word { left: 944px; bottom: 50px; font-family: "Anton", sans-serif; font-size: 42px; color: var(--guest-grey); text-transform: uppercase; }
  .band-name { left: 920px; top: 40px; height: 205px; text-align: left; font-family: "Anton", sans-serif; font-size: 46px; color: var(--white); }
  .pass-type { left: 1040px; bottom: 50px; font-family: "Michroma", sans-serif; font-size: 17px; color: var(--rock-red); font-variant: small-caps; }
</style>
</head>
<body>
  <article class="ticket">
    <svg class="ticket-shape" viewBox="0 0 1100 458" aria-hidden="true">
      <defs>
        <radialGradient id="ticket-fill" cx="45%" cy="45%" r="70%">
          <stop offset="0" stop-color="var(--ticket-mid)"/>
          <stop offset="1" stop-color="var(--ticket-dark)"/>
        </radialGradient>
      </defs>
      <path d="M0 0 H826 L842 18 L858 0 H1100 V458 H858 L842 440 L826 458 H0 Z" fill="url(#ticket-fill)"/>
      <line x1="842" y1="24" x2="842" y2="434" stroke="#e8e8e8" stroke-width="1.5" stroke-dasharray="5 4"/>
    </svg>

    <div class="age">65</div>
    <h1 class="headline">Years and still rocking</h1>
    <h2 class="party-title">Dennis's Birthday Party</h2>
    <div class="rule"></div>

    <div class="guitar" role="img" aria-label="Red electric guitar illustration"></div>

    <section class="details">
      <p class="detail-label">Date &amp; Time</p>
      <p class="detail-bar">Saturday 30 June 2018, 7.00pm - 11.00pm</p>
      <p class="detail-label">Venue</p>
      <p class="detail-bar">Marlow &amp; Fenn Restaurant, 718, Pebble Lane.<br>Clevedon, Auckland 2617</p>
      <p class="detail-label">RSVP</p>
      <p class="detail-bar">RSVP to dennis.halloway@wirefold.co.nz</p>
      <p class="detail-note">Food platter &amp; drink supplied. No presents please</p>
    </section>

    <p class="vertical guest-special">Special</p>
    <p class="vertical guest-word">Guest</p>
    <p class="vertical band-name">Blue Kettle</p>
    <p class="vertical pass-type">VIP Backstage Pass</p>
  </article>
</body>
</html>
```